Visitenkarten-Design für Forschungs- und Beratungsunternehmen
Zielgruppe
*Veridora' ist ein Forschungs- und Beratungsunternehmen für Lebensmittelwirkungen. Unsere Angebote sind: Vorträge, Workshops, Seminare und Coaching. Die Zielgruppen sind Pädagogen, Mediziner, Psychologen u.a.m.
Aufgabenstellung
Bei Bedarf kann die Gestaltung der Visitenkarte auch auf die Rückseite ausgedehnt werden.

```html
<!DOCTYPE html>
<html lang="de">
<head>
<meta charset="utf-8">
<title>Veridora – Visitenkarte</title>
<link rel="stylesheet" href="https://fonts.googleapis.com/css2?family=Montserrat:wght@400;600;700&display=swap">
<style>
  :root {
    --page-bg: #1f1f1f;
    --card-front: #ffffff;
    --card-back: #1c1c1c;
    --ink: #2a2a2a;
    --ink-soft: #555555;
    --rule: #b9b9b9;
    --brand-orange: #f07a1a;
    --brand-purple: #a3338f;
    --brand-on-dark: #f2f2f2;
  }
  * { box-sizing: border-box; margin: 0; padding: 0; }
  html, body {
    width: 1200px; height: 901px; overflow: hidden;
    background: var(--page-bg);
    font-family: "Montserrat", sans-serif;
  }
  .stage {
    position: relative; width: 1200px; height: 901px;
    display: flex; align-items: center; justify-content: center; gap: 60px;
  }
  .card {
    width: 500px; height: 324px; position: relative;
    box-shadow: 0 14px 30px rgba(0,0,0,.45);
  }
  .card--front { background: var(--card-front); }
  .card--back {
    background: var(--card-back);
    display: flex; align-items: center; justify-content: center;
  }
  .brand {
    position: absolute; left: 40px; top: 138px;
    display: flex; align-items: center; gap: 10px;
  }
  .brand__dot {
    width: 22px; height: 22px; border-radius: 50%;
    background: var(--brand-orange);
  }
  .brand__name {
    font-weight: 700; font-size: 24px; color: var(--brand-purple);
  }
  .divider {
    position: absolute; left: 222px; top: 92px;
    width: 2px; height: 146px; background: var(--rule);
  }
  .contact {
    position: absolute; left: 240px; top: 94px; color: var(--ink);
  }
  .contact__name { font-weight: 700; font-size: 19px; }
  .contact__role { font-size: 13px; color: var(--ink-soft); margin-bottom: 12px; }
  .contact__list { list-style: none; }
  .contact__item {
    display: flex; align-items: center; gap: 9px;
    font-size: 13px; line-height: 22px;
  }
  .contact__icon { width: 13px; height: 13px; fill: var(--ink); flex: none; }
  .back-brand { display: flex; align-items: center; gap: 14px; }
  .back-brand__dot {
    width: 30px; height: 30px; border-radius: 50%; background: var(--brand-orange);
  }
  .back-brand__name {
    font-weight: 700; font-size: 40px; color: var(--brand-on-dark);
  }
</style>
</head>
<body>
<main class="stage">
  <section class="card card--front" aria-label="Vorderseite">
    <div class="brand">
      <span class="brand__dot"></span>
      <span class="brand__name">Veridora</span>
    </div>
    <div class="divider"></div>
    <div class="contact">
      <p class="contact__name">Lukas Brenner</p>
      <p class="contact__role">Director</p>
      <ul class="contact__list">
        <li class="contact__item">
          <svg class="contact__icon" viewBox="0 0 24 24"><path d="M6.6 10.8a15.1 15.1 0 0 0 6.6 6.6l2.2-2.2a1 1 0 0 1 1-.25 11.4 11.4 0 0 0 3.6.57 1 1 0 0 1 1 1V20a1 1 0 0 1-1 1A17 17 0 0 1 3 4a1 1 0 0 1 1-1h3.5a1 1 0 0 1 1 1c0 1.25.2 2.45.57 3.57a1 1 0 0 1-.25 1z"/></svg>
          +41 61 555 24 24
        </li>
        <li class="contact__item">
          <svg class="contact__icon" viewBox="0 0 24 24"><path d="M2 5h20v14H2z M2 5l10 8 10-8" fill="none" stroke="currentColor" stroke-width="2"/><rect x="2" y="5" width="20" height="14"/></svg>
          info@veridora.ch
        </li>
        <li class="contact__item">
          <svg class="contact__icon" viewBox="0 0 24 24"><circle cx="12" cy="12" r="10" fill="none" stroke="#2a2a2a" stroke-width="2"/><path d="M2 12h20M12 2c3 3 3 17 0 20M12 2c-3 3-3 17 0 20" fill="none" stroke="#2a2a2a" stroke-width="2"/></svg>
          www.veridora.ch
        </li>
        <li class="contact__item">
          <svg class="contact__icon" viewBox="0 0 24 24"><path d="M12 2a7 7 0 0 0-7 7c0 5 7 13 7 13s7-8 7-13a7 7 0 0 0-7-7zm0 9.5A2.5 2.5 0 1 1 12 6.5a2.5 2.5 0 0 1 0 5z"/></svg>
          CH-4127 Birsdorf
        </li>
      </ul>
    </div>
  </section>

  <section class="card card--back" aria-label="Rückseite">
    <div class="back-brand">
      <span class="back-brand__dot"></span>
      <span class="back-brand__name">Veridora</span>
    </div>
  </section>
</main>
</body>
</html>
```